THE RUBY KITES DANCE CONCERT

Hello again! We need a Front Cover for our Dance Showcase Program. Our theme is year is "LEGENDS" .
We are paying Tribute to the Musical Legends through the years. ORLAND, TOBIAS WRENFIELD, MOSSO, KIRA VELLE etc.
It should include:
1. our Name and Logo (three girls) , which we will provide.
2. Colorful and Bright, Flashy SUPERSTAR feel to it!
3. Size for Print is 8.25 by 10.75 (front page of a magazine type booklet)
4.It should Say somewhere:
" The Ruby Kites Dance Factory presents... "
LEGENDS
5. include "2023 Annual Showcase"
6. Include our website address somewhere : www.RKDFstudios.com
7: include " Follow us @RKDF (Snapwell Logo)
you have been working with us for a few years now. Thank you for sharing your gifts and art!
Music Lovers
Entertainment

```html
<!DOCTYPE html>
<html lang="en">
<head>
<meta charset="utf-8">
<title>Legends – 2023 Annual Showcase Program Cover</title>
<link rel="stylesheet" href="https://fonts.googleapis.com/css2?family=Bebas+Neue&family=Montserrat:wght@400;500;600;800;900&family=Poppins:wght@600;700&display=swap">
<style>
  :root {
    --page-bg: #ffffff;
    --ink: #0b090d;
    --white: #ffffff;
    --magenta: #e02cf0;
    --violet: #7a2bd6;
    --deep-violet: #2a0f3f;
    --band: #1e0d2c;
    --cyan: #37d6f0;
    --ice: #dff8ff;
    --lavender: #d9c8ff;
  }
  * { margin: 0; padding: 0; box-sizing: border-box; }
  html, body {
    width: 1200px; height: 2400px; overflow: hidden;
    background: var(--page-bg);
  }
  .cover {
    position: absolute; left: 80px; top: 521px;
    width: 967px; height: 1262px;
    transform: scale(1.0755); transform-origin: top left;
    background: linear-gradient(180deg, var(--ink) 0%, #14081c 14%, var(--deep-violet) 38%, #2b1240 62%, #1a0c24 80%, var(--ink) 92%);
    overflow: hidden;
    font-family: "Montserrat", sans-serif;
    color: var(--white);
  }
  .stage-lights {
    position: absolute; left: 0; top: 160px; width: 967px; height: 900px;
    background:
      radial-gradient(circle at 9% 34%, rgba(240,60,255,.85), transparent 9%),
      radial-gradient(circle at 91% 40%, rgba(240,60,255,.8), transparent 8%),
      radial-gradient(circle at 73% 28%, rgba(255,80,200,.6), transparent 7%),
      radial-gradient(circle at 28% 20%, rgba(200,60,240,.55), transparent 9%),
      radial-gradient(circle at 5% 62%, rgba(255,245,225,.9), transparent 4%),
      radial-gradient(circle at 92% 55%, rgba(255,245,225,.85), transparent 4%),
      radial-gradient(circle at 66% 47%, rgba(255,240,200,.7), transparent 3.5%),
      radial-gradient(ellipse at 50% 45%, rgba(170,60,240,.55), transparent 55%),
      linear-gradient(180deg, rgba(60,20,80,.15), rgba(120,40,190,.6) 55%, rgba(60,20,110,.45) 80%, transparent);
  }
  .dancers-group {
    position: absolute; left: 70px; top: 190px; width: 770px; height: 500px;
    border-radius: 40% 40% 6% 6% / 30% 30% 4% 4%;
    background: linear-gradient(180deg, rgba(255,255,255,.92), rgba(236,226,255,.88) 70%, rgba(214,196,255,.75));
    box-shadow: 0 0 0 3px rgba(140,80,240,.8), 0 0 30px rgba(120,220,255,.45);
  }
  .title-band { position: absolute; left: 0; top: 0; width: 967px; height: 1262px; }
  .dancers-trio {
    position: absolute; left: 615px; top: 730px; width: 295px; height: 350px;
    border-radius: 46% 46% 10% 10% / 28% 28% 6% 6%;
    background: linear-gradient(180deg, rgba(255,255,255,.95), rgba(236,228,255,.9));
  }
  .studio {
    position: absolute; top: 34px; left: 0; width: 100%;
    text-align: center;
  }
  .studio-name { font-size: 34px; line-height: 42px; font-weight: 600; letter-spacing: 1px; }
  .presents { margin-top: 8px; font-size: 20px; font-weight: 500; letter-spacing: 7px; }
  .year {
    position: absolute; left: 46px; top: 868px;
    font-family: "Bebas Neue", sans-serif; font-size: 164px; line-height: 1;
    color: var(--magenta);
  }
  .event {
    position: absolute; left: 46px; top: 1018px;
    font-weight: 800; font-size: 70px; line-height: 68px; letter-spacing: -1px;
  }
  .tagline {
    position: absolute; left: 48px; top: 1172px;
    font-size: 19px; line-height: 24px; font-weight: 400;
  }
  .contact {
    position: absolute; left: 545px; width: 440px; height: 52px;
    border: 2px solid var(--cyan); border-right: none; border-radius: 8px 0 0 8px;
    display: flex; align-items: center; gap: 12px; padding-left: 12px;
    font-family: "Poppins", sans-serif; font-weight: 700; font-size: 27px;
  }
  .contact-follow { top: 1092px; border-color: var(--cyan); box-shadow: inset 0 -2px 0 var(--magenta); }
  .contact-web { top: 1157px; border-color: var(--magenta); }
  .social-mark {
    width: 28px; height: 28px; border: 3px solid var(--white); border-radius: 7px; flex: none;
  }
  .globe { width: 28px; height: 28px; flex: none; }
</style>
</head>
<body>
  <main class="cover">
    <div class="stage-lights" role="img" aria-label="Purple concert stage lights with glowing bokeh and equalizer bars"></div>
    <div class="dancers-group" role="img" aria-label="White silhouettes of four dancers in energetic poses with neon outlines"></div>

    <svg class="title-band" viewBox="0 0 967 1262">
      <defs>
        <linearGradient id="legendFill" x1="0" y1="1" x2="0" y2="0">
          <stop offset="0" stop-color="#8fe6ff"/>
          <stop offset=".45" stop-color="#ffffff"/>
          <stop offset="1" stop-color="#b04cf0"/>
        </linearGradient>
        <filter id="neonGlow" x="-10%" y="-30%" width="120%" height="160%">
          <feGaussianBlur stdDeviation="8" result="blur"/>
          <feMerge><feMergeNode in="blur"/><feMergeNode in="SourceGraphic"/></feMerge>
        </filter>
      </defs>
      <polygon points="0,700 967,530 967,700 0,875" fill="var(--band)" opacity=".9"/>
      <g transform="translate(68,846) rotate(-11)">
        <text x="9" y="10" font-family="Montserrat, sans-serif" font-weight="900" font-size="172" letter-spacing="-4" fill="var(--violet)">LEGENDS</text>
        <text x="0" y="0" font-family="Montserrat, sans-serif" font-weight="900" font-size="172" letter-spacing="-4" fill="url(#legendFill)" stroke="var(--ice)" stroke-width="3" filter="url(#neonGlow)">LEGENDS</text>
      </g>
    </svg>

    <div class="dancers-trio" role="img" aria-label="Studio emblem: white silhouettes of three girls posing together"></div>

    <header class="studio">
      <p class="studio-name">The Ruby Kites<br>Dance Factory</p>
      <p class="presents">PRESENTS</p>
    </header>

    <p class="year">2023</p>
    <h1 class="event">ANNUAL<br>SHOWCASE</h1>
    <p class="tagline">We are paying Tribute to the Musical<br>Legends through the years.</p>

    <div class="contact contact-follow">
      <span class="social-mark"></span>
      <span>Follow us @RKDF</span>
    </div>
    <div class="contact contact-web">
      <svg class="globe" viewBox="0 0 28 28" fill="none" stroke="#ffffff" stroke-width="2">
        <circle cx="14" cy="14" r="12"/>
        <ellipse cx="14" cy="14" rx="5" ry="12"/>
        <line x1="2" y1="14" x2="26" y2="14"/>
        <line x1="4" y1="8" x2="24" y2="8"/>
        <line x1="4" y1="20" x2="24" y2="20"/>
      </svg>
      <span>www.RKDFstudios.com</span>
    </div>
  </main>
</body>
</html>
```